A new PowerPoint Template for a French consulting company

Who are we?

Formed in 2005, Quorv is a consulting company specialising in the human aspect of change and transformation.

From our offices in the heart of Paris, our team of 30 consultants work with leading organisations in the Aerospace, Finance, Transportation and Public sectors to deliver lasting change.

Our customers trust us with some of their most strategic and sensitive projects. They trust us with these projects because:
- We listen to them, ensuring we understand the real needs of their business
- We involve them, co-developing and tailoring our solutions to the specific challenges they face
- We’re professional, without taking ourselves too seriously
- We’re imaginative, whilst always remaining pragmatic
- We get results!

You can find out more about who we are and the work we do here: http://www.quorv-example.fr/en

What we need from you?

We’re approaching our 10th birthday and, whilst we still love what we do, we think it’s the right time to update our image.

We’d like you to design us a new PowerPoint template, that will be used for all of our internal and client facing work. You can base your submissions on our existing logo and colour scheme (see files attached) or you can submit your own fresh ideas – after all, we’re not afraid of change!

Finally, whilst we’re looking for you to be creative, there are some simple guidelines that we need you to keep in mind:

1. The Template needs to include both a front cover and a “content” page

2. The front cover needs to:
- Include our logo
- Reflect “who we are” and the type of work that we do

3. The content page needs to:
- Have a predominantly white background
- Be practical to use, making an effective use of the 4:3 standard PPT size
- Include an area across the top of the page for the slide title
- Include areas along the bottom of the page for the page number and date

4. If you decide to propose a new colour scheme, it should be balanced and the “accents” usable

5. The PowerPoint Template needs to be “printer friendly”

6. The fonts you use should be standard

What we don’t want?

To give you as much help as possible, here are some things that we really don’t want:

- Submissions that are dull grey or navy blue, suggesting we’re nothing but boring corporate suits
- Submissions that are Lulette pink or too “soft and cuddly”
- Submissions that use lots of stock images of “happy, smiling, consultants”
- Submissions that will be the height of fashion today, but completely out of date next year

```html
<!DOCTYPE html>
<html lang="en">
<head>
<meta charset="utf-8">
<title>Quorv presentation template</title>
<link rel="stylesheet" href="https://fonts.googleapis.com/css2?family=Carlito:ital,wght@0,400;0,700&display=swap">
<style>
  :root {
    --plum: #9c2d63;
    --plum-dark: #5a1f40;
    --footer-plum: #983566;
    --teal: #5aa89d;
    --teal-band: #5f8783;
    --slide-white: #f4f3f1;
    --canvas: #e6e4e1;
  }
  * { margin: 0; padding: 0; box-sizing: border-box; }
  html, body {
    width: 1200px; height: 642px; overflow: hidden;
    background: var(--canvas);
    font-family: "Carlito", "Calibri", sans-serif;
  }
  .stage { position: relative; width: 1200px; height: 642px; }
  .slide {
    position: absolute; top: 55px; width: 499px; height: 353px;
    background: var(--slide-white); overflow: hidden;
    box-shadow: 0 2px 6px rgba(0,0,0,0.18);
  }
  .slide--cover { left: 34px; }
  .slide--content { left: 667px; }
  .slide svg.decor { position: absolute; inset: 0; }

  /* Cover */
  .cover-brand {
    position: absolute; left: 26px; top: 20px;
    font-family: "Carlito", "Calibri", sans-serif;
    font-size: 34px; font-weight: 700; color: var(--plum-dark);
  }
  .cover-title {
    position: absolute; left: 152px; top: 26px;
    font-size: 25px; font-weight: 700; color: var(--plum);
  }
  .cover-subtitle {
    position: absolute; left: 126px; top: 63px; width: 284px; height: 20px;
    background: var(--teal-band); color: #fff;
    font-size: 13px; font-weight: 700; line-height: 20px; padding-left: 26px;
  }

  /* Content */
  .content-brand {
    position: absolute; left: 5px; top: 20px;
    font-family: "Carlito", "Calibri", sans-serif;
    font-size: 14px; font-weight: 700; color: var(--plum-dark);
  }
  .content-title {
    position: absolute; left: 63px; top: 13px;
    font-size: 24px; font-weight: 700; color: var(--plum);
  }
  .content-body { position: absolute; left: 63px; top: 66px; color: var(--plum-dark); }
  .lead { font-size: 18px; font-weight: 700; color: var(--teal); margin-bottom: 3px; }
  .bullets { list-style: none; }
  .bullets li { position: relative; line-height: 1.3; }
  .bullets li::before { position: absolute; color: var(--plum); }
  .level-1 { font-size: 15px; padding-left: 15px; margin-bottom: 3px; }
  .level-1::before { content: "\25C6"; left: 0; font-size: 9px; top: 4px; }
  .level-2 { font-size: 13px; padding-left: 25px; margin-bottom: 3px; }
  .level-2::before { content: "\2013"; left: 15px; }
  .level-3 { font-size: 10px; padding-left: 34px; margin-bottom: 2px; }
  .level-3::before { content: "\2013"; left: 25px; }
  .level-4 { font-size: 9px; padding-left: 39px; }
  .level-4::before { content: "-"; left: 34px; }

  .footer {
    position: absolute; left: 0; bottom: 0; width: 100%; height: 28px;
    background: var(--footer-plum); color: #fff;
  }
  .footer-date {
    position: absolute; left: 0; top: 6px; width: 56px;
    font-size: 7px; line-height: 8px; text-align: center;
  }
  .footer-note {
    position: absolute; left: 0; right: 0; top: 10px;
    font-size: 7px; text-align: center;
  }
  .footer-page { position: absolute; right: 11px; top: 10px; font-size: 7px; }
  .footer svg { position: absolute; inset: 0; }
</style>
</head>
<body>
<main class="stage">

  <section class="slide slide--cover" aria-label="Cover slide">
    <svg class="decor" width="499" height="353" viewBox="0 0 499 353">
      <defs>
        <linearGradient id="cover-photo" x1="0.1" y1="0" x2="0.35" y2="1">
          <stop offset="0" stop-color="#a7b0b3"/>
          <stop offset="0.22" stop-color="#c8cfd0"/>
          <stop offset="0.36" stop-color="#8fbcb4"/>
          <stop offset="0.46" stop-color="#6fa9a0"/>
          <stop offset="0.58" stop-color="#d2d7d7"/>
          <stop offset="0.8" stop-color="#c4c8c9"/>
          <stop offset="0.9" stop-color="#9fa2a3"/>
          <stop offset="1" stop-color="#87898a"/>
        </linearGradient>
      </defs>
      <polygon points="150,0 499,0 499,353 40,353" fill="url(#cover-photo)"
        role="img" aria-label="Photo: a businessman sweeping a teal paint splash across the sky above a grey city skyline"/>
      <line x1="146" y1="0" x2="36" y2="353" stroke="var(--teal)" stroke-width="2"/>
    </svg>
    <div class="cover-brand">Quorv</div>
    <h1 class="cover-title">Title goes here</h1>
    <p class="cover-subtitle">And the subtitle goes here...</p>
  </section>

  <section class="slide slide--content" aria-label="Content slide">
    <svg class="decor" width="498" height="353" viewBox="0 0 498 353">
      <defs>
        <linearGradient id="fade" x1="0" y1="0" x2="0" y2="1">
          <stop offset="0" stop-color="var(--teal)" stop-opacity="0.7"/>
          <stop offset="1" stop-color="var(--teal)" stop-opacity="0"/>
        </linearGradient>
      </defs>
      <line x1="56" y1="0" x2="0" y2="186" stroke="var(--teal)" stroke-width="1.5"/>
      <polygon points="495,0 498,0 445,160 443,160" fill="url(#fade)"/>
    </svg>
    <div class="content-brand">Quorv</div>
    <h2 class="content-title">Slide title goes here</h2>
    <div class="content-body">
      <p class="lead">First sentence</p>
      <ul class="bullets">
        <li class="level-1">Bullet level 1</li>
        <li class="level-2">Bullet level 2</li>
        <li class="level-3">Bullet level 3</li>
        <li class="level-4">Bullet level 4</li>
      </ul>
    </div>
    <footer class="footer">
      <svg width="498" height="28" viewBox="0 0 498 28">
        <g stroke="#fff" stroke-width="1" opacity="0.85">
          <line x1="64" y1="0" x2="56" y2="28"/>
          <line x1="68" y1="0" x2="60" y2="28"/>
          <line x1="72" y1="0" x2="64" y2="28"/>
          <line x1="472" y1="0" x2="464" y2="28"/>
        </g>
      </svg>
      <p class="footer-date">September 12,<br>2014</p>
      <p class="footer-note">Of course we also have a footer</p>
      <p class="footer-page">2</p>
    </footer>
  </section>

</main>
</body>
</html>
```